Korvane Sky Works, LLC - Business Card

I currently have a drone business that specializes in aerial photography, thermal image inspections, deer recovery, search and rescue, custom agricultural applications. i will attach my current business card as well as some logos to incorporate for a new up to date business card
Updates

Designs look the same

Sick

Target Market(s)

farmers, hunters

Contact Information for Business Card

name address phone number (as existing card i attached)

Requirements
Must have
• im good with existing business card, but would like an agricultural twist

```html
<!DOCTYPE html>
<html lang="en">
<head>
<meta charset="utf-8">
<title>Korvane Sky Works, LLC – Business Card</title>
<link href="https://fonts.googleapis.com/css2?family=Open+Sans:wght@400;600;800&display=swap" rel="stylesheet">
<style>
  :root {
    --page: #2a2a2a;
    --card: #ffffff;
    --orange: #ff8a00;
    --amber: #ffb000;
    --yellow: #ffcc00;
    --sun: #ff6400;
    --green: #5a9e1f;
    --green-light: #7dbb3c;
    --ink: #1c1c1c;
  }
  * { margin: 0; padding: 0; box-sizing: border-box; }
  html, body { width: 1200px; height: 960px; overflow: hidden; background: var(--page); }
  body { font-family: "Open Sans", sans-serif; color: var(--ink); }
  .canvas { position: relative; width: 1200px; height: 960px; }
  .card {
    position: absolute; left: 230px; width: 740px; height: 423px;
    background: var(--card); overflow: hidden;
    box-shadow: 0 10px 30px rgba(0,0,0,.5);
  }
  .card--front { top: 40px; }
  .card--back { top: 497px; }
  .card__art { position: absolute; inset: 0; width: 100%; height: 100%; }
  .brand {
    position: absolute; display: flex; align-items: center; gap: 8px;
    font-weight: 800; color: var(--green); line-height: 1;
  }
  .brand__dot { border-radius: 50%; border: 3px solid var(--green); }
  .card--front .brand { left: 118px; top: 160px; font-size: 22px; }
  .card--front .brand__dot { width: 22px; height: 22px; }
  .card--back .brand { left: 50%; top: 190px; transform: translateX(-50%); font-size: 44px; }
  .card--back .brand__dot { width: 40px; height: 40px; border-width: 4px; }
  .person { position: absolute; left: 340px; top: 68px; }
  .person__name { font-size: 26px; font-weight: 800; letter-spacing: .5px; line-height: 1; }
  .person__name .surname { color: var(--green); }
  .person__role { font-size: 12px; font-weight: 600; color: var(--green); margin-top: 2px; }
  .contacts { position: absolute; left: 370px; top: 118px; list-style: none; }
  .contacts li { display: flex; align-items: flex-start; gap: 10px; font-size: 16px; line-height: 1.25; margin-bottom: 6px; }
  .contacts svg { flex: none; width: 16px; height: 16px; margin-top: 2px; }
  .services { position: absolute; left: 112px; top: 204px; list-style: none; }
  .services li { font-size: 16px; line-height: 1.5; }
  .services li::before { content: "•"; color: var(--green); margin-right: 7px; font-weight: 800; }
</style>
</head>
<body>
<main class="canvas">
  <svg width="0" height="0" style="position:absolute" aria-hidden="true">
    <defs>
      <radialGradient id="sun-glow-front" cx="0.55" cy="0.35" r="0.9">
        <stop offset="0" stop-color="var(--sun)"/>
        <stop offset="0.35" stop-color="var(--yellow)"/>
        <stop offset="1" stop-color="var(--orange)"/>
      </radialGradient>
      <radialGradient id="sun-glow-back" cx="0.5" cy="0.3" r="0.9">
        <stop offset="0" stop-color="var(--sun)"/>
        <stop offset="0.35" stop-color="var(--yellow)"/>
        <stop offset="1" stop-color="var(--orange)"/>
      </radialGradient>
      <linearGradient id="field-glow" x1="0" y1="1" x2="1" y2="0">
        <stop offset="0" stop-color="var(--green)"/>
        <stop offset="1" stop-color="var(--green-light)"/>
      </linearGradient>
    </defs>
  </svg>

  <!-- Front -->
  <section class="card card--front">
    <svg class="card__art" viewBox="0 0 740 423">
      <polygon role="img" aria-label="Sunrise rays in orange and yellow" fill="url(#sun-glow-front)" points="0,0 290,0 0,122"/>
      <polygon role="img" aria-label="Sunrise rays in orange" fill="url(#sun-glow-front)" points="470,0 740,0 740,44"/>
      <polygon class="band band--orange" fill="var(--orange)" points="0,132 310,0 420,0 0,180"/>
      <polygon class="band band--green" fill="var(--green)" points="0,372 740,232 740,262 0,402"/>
      <polygon role="img" aria-label="Green field rows" fill="url(#field-glow)" points="0,410 740,270 740,423 0,423"/>
    </svg>

    <div class="brand"><span class="brand__dot"></span>Korvane</div>

    <div class="person">
      <h1 class="person__name">DALEN <span class="surname">MARSH</span></h1>
      <p class="person__role">Owner</p>
    </div>

    <ul class="contacts">
      <li><svg viewBox="0 0 16 16"><circle cx="8" cy="8" r="7.5" fill="none" stroke="var(--green)"/><path d="M5 4.5l1.6-.4.8 2-1 .8a5 5 0 0 0 2.7 2.7l.8-1 2 .8-.4 1.6C8 11.6 4.4 8 5 4.5z" fill="var(--green)"/></svg>419-555-0148</li>
      <li><svg viewBox="0 0 16 16" fill="none" stroke="var(--green)"><circle cx="8" cy="8" r="7.5"/><circle cx="8" cy="8" r="4.5"/><path d="M3.5 8h9M8 3.5c-2 2.5-2 6.5 0 9M8 3.5c2 2.5 2 6.5 0 9"/></svg>www.korvaneskyworks.com</li>
      <li><svg viewBox="0 0 16 16" fill="none" stroke="var(--green)"><circle cx="8" cy="8" r="7.5"/><rect x="4" y="5.5" width="8" height="5.5"/><path d="M4 5.5l4 3 4-3"/></svg>korvaneskyworks@mailbox.com</li>
      <li><svg viewBox="0 0 16 16"><circle cx="8" cy="8" r="7.5" fill="none" stroke="var(--green)"/><path d="M8 3.5a3 3 0 0 1 3 3c0 2.2-3 5.5-3 5.5S5 8.7 5 6.5a3 3 0 0 1 3-3z" fill="var(--green)"/><circle cx="8" cy="6.5" r="1" fill="#fff"/></svg><span>214 W. Orchard St.<br>Fenwick, OH 45390</span></li>
    </ul>

    <ul class="services">
      <li>Thermal Image Inspections</li>
      <li>Deer Recovery</li>
      <li>Search &amp; Rescue</li>
      <li>Real Estate Photography</li>
    </ul>
  </section>

  <!-- Back -->
  <section class="card card--back">
    <svg class="card__art" viewBox="0 0 740 423">
      <polygon role="img" aria-label="Sunrise rays in orange and yellow" fill="url(#sun-glow-back)" points="0,0 360,0 0,140"/>
      <polygon role="img" aria-label="Sunrise rays in orange" fill="url(#sun-glow-back)" points="500,0 740,0 740,100"/>
      <polygon class="band band--orange" fill="var(--orange)" points="0,150 385,0 480,0 0,196"/>
      <polygon class="band band--green" fill="var(--green)" points="0,390 740,190 740,222 0,422"/>
      <polygon role="img" aria-label="Green field rows" fill="url(#field-glow)" points="0,430 740,230 740,423 0,423"/>
    </svg>

    <div class="brand"><span class="brand__dot"></span>Korvane</div>
  </section>
</main>
</body>
</html>
```